Kovala RQNV Magazine Cover style graphic.

I am looking to create a document cover.
Brantley Solutions
The True Cost of an Embroidery Machineā€
Subtitle: Why the Lowest Upfront Price Can Become the Most Expensive Decision. Using Brantley logo's and Kovala RQNV for a high impact cover. It should look like a magazine cover. This is the most advance technology available for the embroidery industry. We want to portray this as a platform and not simply a machine. We will have an 8 page guide.

Target Market(s)

Our customer base

Industry/Entity Type

Industrial Embroidery

Font styles to use
Serif

Colors
0054AA
0677BA
7BADD7
CADEEF
E8F1F8

Requirements
Must have
• High impact, visually pleasing cover.

```html
<!DOCTYPE html>
<html lang="en">
<head>
<meta charset="utf-8">
<title>The True Cost of an Embroidery Machine — Brantley Solutions</title>
<link href="https://fonts.googleapis.com/css2?family=Montserrat:wght@300;400;800&display=swap" rel="stylesheet">
<style>
  :root {
    --blue-deep: #0054AA;
    --blue-mid: #0677BA;
    --blue-soft: #7BADD7;
    --blue-pale: #CADEEF;
    --blue-mist: #E8F1F8;
    --white: #ffffff;
    --brand-magenta: #b0237a;
  }
  * { margin: 0; padding: 0; box-sizing: border-box; }
  html, body { width: 849px; height: 1200px; overflow: hidden; background: var(--white); }
  .cover {
    position: relative;
    width: 849px;
    height: 1200px;
    overflow: hidden;
    font-family: "Montserrat", Arial, sans-serif;
    background: linear-gradient(180deg, var(--blue-mid) 0%, #2c8fd0 28%, var(--blue-soft) 58%, var(--blue-pale) 72%, var(--blue-mist) 78%, var(--white) 82%);
  }
  .lace-texture {
    position: absolute;
    left: 0; top: 420px;
    width: 520px; height: 560px;
    background: radial-gradient(ellipse at 45% 45%, rgba(232,241,248,0.55) 0%, rgba(202,222,239,0.25) 45%, rgba(123,173,215,0) 75%);
  }
  .brand-mark {
    position: absolute;
    top: 42px; right: 52px;
    display: flex; align-items: center; gap: 12px;
    color: var(--white);
    font-weight: 800;
    font-size: 28px;
    line-height: 1;
    text-transform: uppercase;
  }
  .brand-mark .square { width: 42px; height: 42px; background: var(--white); }
  .brand-mark .name { display: flex; flex-direction: column; gap: 4px; }
  .headline {
    position: absolute; top: 150px; right: 49px;
    text-align: right; color: var(--white);
  }
  .headline .lead {
    display: block;
    font-weight: 300; font-size: 58px; line-height: 1.1; letter-spacing: -0.5px;
  }
  .headline .main {
    display: block;
    font-weight: 800; font-size: 100px; line-height: 0.96; letter-spacing: 1px;
    margin-top: 6px;
  }
  .subtitle {
    position: absolute; top: 420px; right: 56px;
    width: 340px; text-align: right;
    color: var(--white); font-size: 22px; line-height: 1.15; font-weight: 400;
  }
  .machine-photo {
    position: absolute; left: 380px; top: 515px;
    width: 440px; height: 645px;
    background: linear-gradient(180deg, #eef1f4 0%, #d9dde2 55%, #c8ccd2 100%);
    border-radius: 6px;
  }
  .partner-mark {
    position: absolute; left: 40px; bottom: 50px;
    display: flex; align-items: center; gap: 10px;
    color: var(--brand-magenta); font-weight: 800; font-size: 26px;
    text-transform: uppercase;
  }
  .partner-mark .square { width: 28px; height: 28px; background: var(--brand-magenta); }
</style>
</head>
<body>
<main class="cover">
  <div class="lace-texture" role="img" aria-label="Close-up of white lace embroidery on fabric, faded into the blue background"></div>

  <div class="brand-mark">
    <span class="square"></span>
    <span class="name"><span>Brantley</span><span>Solutions</span></span>
  </div>

  <h1 class="headline">
    <span class="lead">The True Cost of an</span>
    <span class="main">EMBROIDERY<br>MACHINE</span>
  </h1>

  <p class="subtitle">Why the Lowest Upfront Price Can Become the Most Expensive Decision</p>

  <div class="machine-photo" role="img" aria-label="Kovala RQNV single-head multi-needle embroidery machine on a stand, with touchscreen panel and a purple garment hooped"></div>

  <div class="partner-mark">
    <span class="square"></span>
    <span>Kovala</span>
  </div>
</main>
</body>
</html>
```